Heron's Weir Whisky Label

Create a label for a new craft whisky from the Marlbeck Distilling Company (see attached logo). It should reflect country and historical values (Heron's Weir was the site of violent confrontations during the English Civil War in 1642 (description attached). It should incorporate the name of the whisky (Heron's Weir Whisky) and the description, below, of the product - "Hollowmere Single Malt". It should also feature the logo of the company, and we would like the label background to incorporate one of the 2 photos (attached) of Heron's Weir.
Please note that a drawing, with specifications, of the bottle have just been uploaded.

```html
<!DOCTYPE html>
<html lang="en">
<head>
<meta charset="utf-8">
<title>Heron's Weir Whisky Label</title>
<link rel="stylesheet" href="https://fonts.googleapis.com/css2?family=Playball&family=Cormorant+Garamond:wght@600&family=Rye&family=Josefin+Sans:wght@400;600&family=Montserrat:wght@800&family=Italianno&display=swap">
<style>
  :root {
    --paper: #ebe5d8;
    --paper-edge: #d4cab5;
    --ink: #3a332b;
    --ink-soft: #5b5246;
    --western: #8b806f;
    --sepia-dark: #2f2a24;
    --sepia-mid: #7d7466;
    --sepia-light: #c9c1b2;
    --frame: #8f8574;
    --frame-light: #b4aa97;
    --badge: #f4f1ea;
  }
  * { margin: 0; padding: 0; box-sizing: border-box; }
  html, body { width: 833px; height: 1200px; overflow: hidden; background: var(--paper); }
  .label {
    position: relative; width: 833px; height: 1200px; overflow: hidden;
    background: radial-gradient(ellipse at 50% 45%, var(--paper) 45%, var(--paper-edge) 100%);
    color: var(--ink);
  }
  .rules { position: absolute; inset: 0; }
  .flourish {
    position: absolute; left: 50%; transform: translateX(-50%);
    width: 400px; height: 46px; border-radius: 23px;
    background: linear-gradient(90deg, transparent, rgba(58,51,43,.35) 20%, rgba(58,51,43,.45) 50%, rgba(58,51,43,.35) 80%, transparent);
  }
  .flourish--top { top: 30px; }
  .flourish--bottom { top: 1112px; width: 434px; }
  .photo {
    position: absolute; left: 122px; top: 110px; width: 566px; height: 392px;
    background:
      radial-gradient(ellipse at 30% 35%, var(--sepia-mid) 0%, transparent 55%),
      linear-gradient(180deg, var(--sepia-dark) 0%, #4a4339 45%, var(--sepia-light) 78%, #9d9485 100%);
    box-shadow: 0 0 14px 4px rgba(47,42,36,.35);
  }
  .frame {
    position: absolute; left: 41px; top: 515px; width: 756px; height: 585px;
    border-radius: 120px / 110px;
    border: 34px solid var(--frame);
    background: transparent;
    box-shadow: inset 0 0 0 4px var(--frame-light), 0 0 0 4px var(--frame-light);
    opacity: .75;
  }
  .panel { position: absolute; left: 0; width: 833px; text-align: center; }
  .the {
    top: 606px; font-family: "Playball", cursive; font-size: 74px; line-height: 1; color: var(--ink);
  }
  .subtitle {
    top: 696px; font-family: "Cormorant Garamond", serif; font-weight: 600; font-size: 25px;
    letter-spacing: 3px; color: var(--ink-soft);
  }
  .product-name {
    top: 762px; font-family: "Rye", serif; font-weight: 400; font-size: 40px; letter-spacing: 1px; color: var(--western);
  }
  .tagline {
    top: 842px; font-family: "Josefin Sans", sans-serif; font-size: 14px; letter-spacing: .3px; color: var(--ink-soft);
  }
  .tagline .script { font-family: "Playball", cursive; font-size: 20px; letter-spacing: 0; margin-right: 14px; }
  .tagline .dot { margin-right: 14px; }
  .brand {
    top: 874px; font-family: "Josefin Sans", sans-serif; font-weight: 600; font-size: 21px; letter-spacing: 5px; color: var(--ink-soft);
  }
  .quality {
    top: 912px; font-family: "Josefin Sans", sans-serif; font-weight: 600; font-size: 18px; letter-spacing: 1px; color: var(--ink);
  }
  .quality .heavy { font-family: "Montserrat", sans-serif; font-weight: 800; font-size: 20px; margin-left: 10px; }
  .descriptor {
    top: 944px; font-family: "Italianno", cursive; font-size: 46px; line-height: 1; color: var(--western);
  }
  .maker {
    position: absolute; left: 37px; top: 917px; width: 188px; height: 188px; border-radius: 50%;
    background: var(--badge); border: 5px solid var(--frame);
    display: flex; align-items: center; justify-content: center; text-align: center;
    font-family: "Josefin Sans", sans-serif; font-weight: 600; font-size: 17px; line-height: 1.25;
    letter-spacing: 1px; color: var(--ink); padding: 24px;
  }
</style>
</head>
<body>
<main class="label">
  <svg class="rules" width="833" height="1200" viewBox="0 0 833 1200" aria-hidden="true">
    <g fill="var(--ink)" stroke="var(--ink)">
      <line x1="21" y1="44" x2="21" y2="1156" stroke-width="2.5"/>
      <line x1="811" y1="44" x2="811" y2="1156" stroke-width="2.5"/>
      <path d="M21 36 L15 54 L21 49 L27 54 Z" stroke="none"/>
      <path d="M811 36 L805 54 L811 49 L817 54 Z" stroke="none"/>
      <path d="M21 1164 L15 1146 L21 1151 L27 1146 Z" stroke="none"/>
      <path d="M811 1164 L805 1146 L811 1151 L817 1146 Z" stroke="none"/>
      <circle cx="21" cy="120" r="6" stroke="none"/>
      <circle cx="811" cy="120" r="6" stroke="none"/>
      <circle cx="21" cy="1057" r="6" stroke="none"/>
      <circle cx="811" cy="1057" r="6" stroke="none"/>
    </g>
  </svg>

  <div class="flourish flourish--top" role="img" aria-label="Decorative scrollwork flourish"></div>

  <div class="photo" role="img" aria-label="Sepia photograph of Heron's Weir: a wooded country lane crossing a small stone bridge beneath dense trees"></div>

  <div class="frame" role="img" aria-label="Ornate engraved Victorian scroll frame"></div>

  <div class="panel the">The</div>
  <div class="panel subtitle">PLACE YOUR TEXT HERE</div>
  <h1 class="panel product-name">HERON'S WEIR WHISKY</h1>
  <p class="panel tagline"><span class="script">Premium Quality</span><span class="dot">•</span>TRADEMARKED IN THE LOREM IPSUM, REGISTERED DOLOR SIT</p>
  <p class="panel brand">•ORIGINAL BRAND•</p>
  <p class="panel quality">QUALITY ★ CO. <span class="heavy">PREMIUM</span> EST. '36</p>
  <p class="panel descriptor">Hollowmere Single Malt</p>

  <div class="maker">Marlbeck Distilling Company</div>

  <div class="flourish flourish--bottom" role="img" aria-label="Decorative scrollwork flourish"></div>
</main>
</body>
</html>
```